Business Card for a new businees.

need a very good business for a new company based in Riverside California call Levy Lantern LLC. We help client file taxes, resolve tax debt and attain peace of mind We help people nationwide solve Tax problems. We help with Installment agreements, Offers in Compromise, Partial Pay Installment Agreements, Currently Not Collectible status, Liens and Levy Removal, Garnishment removal. We offer individualized services

Target Market(s)

Any one with Tax Problems nationwide. My clients span across age, occupation etc

Contact Information for Business Card

Card must be attractive and have enough information to let client know we care and call us

Colors

Designer to choose colors to be used in the design.

Requirements
Must have
• the basics and then surprise me
Nice to have
• surprise m

```html
<!DOCTYPE html>
<html lang="en">
<head>
<meta charset="utf-8">
<title>Levy Lantern LLC — Business Card</title>
<link href="https://fonts.googleapis.com/css2?family=Ubuntu:wght@400;500;700&family=Open+Sans:wght@400;600&display=swap" rel="stylesheet">
<style>
  :root {
    --page: #dcd6cd;
    --card: #0c0c0b;
    --card-glow: #1e1e12;
    --gold: #e6c43a;
    --yellow: #f5d43e;
    --olive: #b9b45a;
    --white: #f4f4f0;
  }
  * { box-sizing: border-box; margin: 0; padding: 0; }
  html, body { width: 1200px; height: 1200px; overflow: hidden; }
  body {
    background: var(--page);
    font-family: "Ubuntu", sans-serif;
    position: relative;
  }
  .card {
    position: absolute;
    left: 150px;
    width: 900px;
    height: 514px;
    background: radial-gradient(ellipse at 45% 50%, var(--card-glow) 0%, var(--card) 65%);
    overflow: hidden;
    box-shadow: 0 10px 30px rgba(0,0,0,0.25);
  }
  .card--front { top: 60px; }
  .card--back  { top: 626px; }

  .brand {
    position: absolute;
    left: 150px;
    top: 165px;
    display: flex;
    flex-direction: column;
  }
  .brand__name {
    display: flex;
    align-items: center;
    gap: 16px;
    font-weight: 500;
    font-size: 58px;
    color: var(--gold);
    letter-spacing: 0.5px;
    line-height: 1;
  }
  .brand__dot {
    width: 34px; height: 34px;
    border-radius: 50%;
    background: var(--gold);
    flex: none;
  }
  .brand__rule {
    height: 6px;
    background: var(--yellow);
    margin: 18px 0 14px 50px;
    width: 300px;
  }
  .brand__tagline {
    margin-left: 50px;
    font-family: "Open Sans", sans-serif;
    font-weight: 600;
    font-size: 17px;
    letter-spacing: 4px;
    color: var(--white);
  }
  .brand__slogan {
    margin-left: 50px;
    margin-top: 6px;
    font-size: 13px;
    letter-spacing: 1px;
    color: var(--olive);
    text-transform: uppercase;
  }
  .card--back .brand { top: 120px; }

  .accent {
    position: absolute;
    background: var(--yellow);
  }
  .accent--name    { left: 0; bottom: 30px; width: 54px; height: 36px; }
  .accent--contact { right: 0; bottom: 40px; width: 18px; height: 48px; }

  .holder {
    position: absolute;
    left: 74px;
    bottom: 38px;
  }
  .holder__name {
    font-weight: 700;
    font-size: 26px;
    color: var(--yellow);
  }
  .holder__role {
    font-family: "Open Sans", sans-serif;
    font-size: 16px;
    color: var(--white);
    margin-top: 2px;
  }

  .contact {
    position: absolute;
    right: 40px;
    bottom: 36px;
    display: grid;
    grid-template-columns: auto auto;
    column-gap: 36px;
    row-gap: 10px;
    font-family: "Open Sans", sans-serif;
    font-size: 16px;
  }
  .contact__item {
    display: flex;
    align-items: center;
    gap: 10px;
    color: var(--gold);
    white-space: nowrap;
  }
  .contact__item svg { width: 18px; height: 18px; flex: none; }
</style>
</head>
<body>

  <section class="card card--front" aria-label="Card front">
    <div class="brand">
      <div class="brand__name"><span class="brand__dot"></span>Levy Lantern LLC</div>
      <div class="brand__rule"></div>
      <div class="brand__tagline">DEBT RELIEF. TAX RETURNS.</div>
      <div class="brand__slogan">Nationwide tax relief, one client at a time</div>
    </div>
  </section>

  <section class="card card--back" aria-label="Card back">
    <div class="brand">
      <div class="brand__name"><span class="brand__dot"></span>Levy Lantern LLC</div>
      <div class="brand__rule"></div>
      <div class="brand__tagline">DEBT RELIEF. TAX RETURNS.</div>
      <div class="brand__slogan">Nationwide tax relief, one client at a time</div>
    </div>

    <div class="accent accent--name"></div>
    <div class="holder">
      <div class="holder__name">Dana Reyes</div>
      <div class="holder__role">Director</div>
    </div>

    <div class="contact">
      <div class="contact__item">
        <svg viewBox="0 0 24 24" fill="#f4f4f0"><path d="M6.6 10.8a15.1 15.1 0 0 0 6.6 6.6l2.2-2.2a1 1 0 0 1 1-.25 11.4 11.4 0 0 0 3.6.57 1 1 0 0 1 1 1V20a1 1 0 0 1-1 1A17 17 0 0 1 3 4a1 1 0 0 1 1-1h3.5a1 1 0 0 1 1 1c0 1.25.2 2.45.57 3.57a1 1 0 0 1-.25 1z"/></svg>
        +XXX XX XXX XXX
      </div>
      <div class="contact__item">
        <svg viewBox="0 0 24 24" fill="none" stroke="#f4f4f0" stroke-width="2"><rect x="3" y="5" width="18" height="14" rx="1"/><path d="M3 6l9 7 9-7"/></svg>
        hello@levylantern.com
      </div>
      <div class="contact__item">
        <svg viewBox="0 0 24 24" fill="none" stroke="#f4f4f0" stroke-width="2"><rect x="4" y="8" width="16" height="12" rx="2"/><path d="M7 8V5h10v3"/><circle cx="12" cy="14" r="2.5"/></svg>
        +XXX XX XXX XXX
      </div>
      <div class="contact__item">
        <svg viewBox="0 0 24 24" fill="none" stroke="#f4f4f0" stroke-width="2"><circle cx="12" cy="12" r="9"/><path d="M3 12h18M12 3c3 3.2 3 14.8 0 18M12 3c-3 3.2-3 14.8 0 18"/></svg>
        www.levylantern.com
      </div>
    </div>
    <div class="accent accent--contact"></div>
  </section>

</body>
</html>
```